The Mariposa - Print identity

The Mariposa is a mixed-use commercial/residential condo building in beautiful Vancouver. It is a fantastic exemple of mid-century modern architecture (built in 1955 as the HQ of the Northfield Power Works Corp., it was converted to condos in 1995) and has several valuable architectural elements. It is a landmark building in the downtown core.

Although we have a wordmark and other graphic collateral we need to retain, as we reorganized the management of the building we wish to refresh the print- (and online) communication with a splash of colour, professionalism and consistency to indicate things are now different. (Thus far it's been left to anyone to put together logos, fonts and colours sometimes to horrific results!)

We are very proud of our building and its heritage: please seek inspiration in the images attached.

Merci
Mathieu

Target Market(s)

Mid-30's professional downtown dwellers.
Values: Reliable, solid, well-managed, good value, long-lasting, sleek, clean, modern with an edge.

Industry/Entity Type

Real Estate

Requirements
Must have
• 1/ Reuse "The Mariposa" wordmark. Other collateral optional but simpler is better.
• 2/ Prepare at least one design for a letter-size (8.5X11) multi-purpose document (bulletin/memo/newsletter/letterhead) in colour & B/W versions.
Nice to have
• 1/ Design should be easily transferable to website and email newsletter.
• 2/ MS Word and/or html template would be nice rather than graphic file.
• 3/ Font/size, layout, titles and formatting suggestions would be awesome to make suitable for 'sample usage' docs provided.
• 4/ Option to include/exclude sender address depending if used for letterhead or bulletin/newsletter
• 5/ Building is managed by 3rd party - include footnote or sidebar with "Proudly managed by BrenTor Coastal. Lou Dane, Senior Property Manager" type of mention (no vector logo file currently available, use placeholder)

```html
<!DOCTYPE html>
<html lang="en">
<head>
<meta charset="utf-8">
<title>The Mariposa – Letterhead</title>
<link rel="stylesheet" href="https://fonts.googleapis.com/css2?family=Poiret+One&display=swap">
<style>
  :root {
    --backdrop: #ffffff;
    --paper: #ffffff;
    --paper-edge: #e9dfc6;
    --ink: #141414;
    --gold: #c98a2e;
    --gold-pale: #f3e6d0;
    --sepia-dark: #7a5a3e;
    --sepia-light: #e6d6c4;
    --outline-tint: #fbe9dc;
  }
  html, body {
    margin: 0;
    width: 1034px;
    height: 1200px;
    overflow: hidden;
    background: var(--backdrop);
  }
  .letterhead {
    position: absolute;
    left: 103px;
    top: 60px;
    width: 828px;
    height: 1078px;
    background: var(--paper);
    border: 1px solid var(--paper-edge);
    box-shadow: 0 0 10px 3px rgba(214, 196, 150, 0.55);
    overflow: hidden;
  }
  .wordmark {
    position: absolute;
    right: 318px;
    top: 82px;
    margin: 0;
    font-family: "Poiret One", sans-serif;
    font-weight: 400;
    font-size: 44px;
    letter-spacing: 0;
    line-height: 1;
    color: var(--ink);
    white-space: nowrap;
  }
  .tower-photo {
    position: absolute;
    left: 522px;
    top: 5px;
    width: 70px;
    height: 130px;
    background: linear-gradient(90deg, var(--sepia-dark), #b48a63 55%, #efe2d2);
    clip-path: polygon(10% 4%, 62% 0, 100% 20%, 100% 100%, 6% 100%);
  }
  .rule {
    position: absolute;
    top: 125px;
    height: 4px;
  }
  .rule--left {
    left: 4px;
    width: 516px;
    background: linear-gradient(90deg, rgba(255,255,255,0), var(--gold-pale) 25%, #e2b777);
  }
  .rule--right {
    left: 596px;
    width: 232px;
    background: var(--gold);
  }
  .corner-tower {
    position: absolute;
    left: 0;
    top: 680px;
    width: 160px;
    height: 398px;
    background: linear-gradient(90deg, var(--sepia-light), #f7f0e8 70%, rgba(255,255,255,0));
    clip-path: polygon(0 0, 88% 50%, 92% 100%, 0 100%);
  }
  .side-elevation {
    position: absolute;
    left: 745px;
    top: 145px;
    width: 83px;
    height: 925px;
    background: linear-gradient(90deg, rgba(251,233,220,0), var(--outline-tint));
  }
</style>
</head>
<body>
  <main class="letterhead">
    <h1 class="wordmark">The Mariposa</h1>
    <div class="tower-photo" role="img" aria-label="Sepia photograph of The Mariposa tower"></div>
    <div class="rule rule--left"></div>
    <div class="rule rule--right"></div>
    <div class="corner-tower" role="img" aria-label="Faded photograph of the building facade rising from the lower left corner"></div>
    <div class="side-elevation" role="img" aria-label="Faint architectural elevation outline of the building along the right edge"></div>
  </main>
</body>
</html>
```